Business Card Design: recruitment/consultancy for business Harbor720more

We need a business card design for a new company based in Adelaide Australia called Harbor720more. Our Business aims to support people over 50 who may be looking for a career change, have been made redundant or generally looking for employment. We will also be working with businesses to provide them with recruiting solutions, job design, recruitment strategies and customised training. we will also be working with volunteering opportunities for those over 50.
We would like to see the E in harbor720more strong and dominant. The final design should reflect change for the better, better opportunities, today is the day, make way for the new, all aimed at the 50 plus age group.
Colours we are thinking off include green (money, growth) black and white.... we like the idea of black and white photography with a one dominant colour...think of a of a black and white photo of a woman with dominant red lips...that sort of look

Business

Dev, Mabel & Joan
phone: 0498163520
Harbor720more@mailbox-demo.com
Social/Harbor720more
www.harbor720more-demo.com.au

```html
<!DOCTYPE html>
<html lang="en">
<head>
<meta charset="utf-8">
<title>Harbor720more – Business Card</title>
<link href="https://fonts.googleapis.com/css2?family=Barlow:wght@400;500;600&family=Barlow+Condensed:wght@700&display=swap" rel="stylesheet">
<style>
  :root {
    --backdrop: #e9e9ec;
    --card-white: #ffffff;
    --ink: #1c1c1c;
    --ink-soft: #3a3a3a;
    --brand-green: #1aa37a;
    --mint-band: #dcefe9;
    --accent-red: #e3262b;
    --photo-light: #d9d9d9;
    --photo-mid: #9c9c9c;
    --photo-dark: #6b6b6b;
  }
  * { box-sizing: border-box; margin: 0; padding: 0; }
  html, body {
    width: 1200px; height: 800px; overflow: hidden;
    background: var(--backdrop);
    font-family: "Barlow", Arial, sans-serif;
    color: var(--ink);
  }
  .stage {
    position: relative; width: 1200px; height: 800px;
    display: flex; align-items: center; justify-content: center; gap: 60px;
  }
  .card {
    position: relative; width: 520px; height: 318px; overflow: hidden;
    background: var(--card-white);
    box-shadow: 0 10px 28px rgba(0,0,0,.18);
  }

  /* Front */
  .card-front .photo-fill {
    position: absolute; inset: 0;
    background: linear-gradient(120deg, var(--photo-mid) 0%, var(--photo-light) 45%, var(--photo-mid) 75%, var(--photo-dark) 100%);
  }
  .card-front .wordmark {
    position: absolute; left: 130px; top: 88px;
    font-weight: 600; font-size: 44px; letter-spacing: .5px; color: var(--ink);
  }
  .service-list {
    position: absolute; left: 26px; top: 156px; list-style: none;
    font-size: 14px; font-weight: 500; line-height: 20px; color: var(--ink);
  }
  .service-list li { display: flex; align-items: center; gap: 7px; }
  .service-list li::before {
    content: ""; width: 11px; height: 11px; border-radius: 50%;
    background: var(--accent-red); flex: none;
  }
  .card-front .website {
    position: absolute; left: 26px; top: 230px;
    font-size: 16px; font-weight: 600; color: var(--ink);
  }
  .tagline-tab {
    position: absolute; right: 0; bottom: 0; width: 170px; height: 40px;
    background: var(--brand-green); color: var(--card-white);
    border-top-left-radius: 26px;
    display: flex; align-items: center; justify-content: center;
    font-size: 16px; font-weight: 600;
  }

  /* Back */
  .mint-band {
    position: absolute; left: 0; right: 0; top: 70px; height: 110px;
    background: linear-gradient(90deg, var(--mint-band), #eef8f5);
  }
  .partner-names {
    position: absolute; right: 24px; top: 82px;
    font-family: "Barlow Condensed", Arial, sans-serif;
    font-weight: 700; font-size: 17px; letter-spacing: .5px; text-transform: uppercase;
  }
  .card-back .wordmark {
    position: absolute; left: 60px; top: 112px;
    display: flex; align-items: center; gap: 10px;
    font-weight: 600; font-size: 44px; letter-spacing: .5px; color: var(--ink);
  }
  .card-back .wordmark::before {
    content: ""; width: 18px; height: 18px; border-radius: 50%; background: var(--brand-green);
  }
  .contact-list {
    position: absolute; left: 32px; top: 200px;
    font-size: 15px; line-height: 21px; color: var(--ink-soft); font-style: normal;
  }
</style>
</head>
<body>
<main class="stage">
  <section class="card card-front">
    <div class="photo-fill" role="img" aria-label="Black and white photograph of three smiling mature workers, two wearing hard hats, on a building site"></div>
    <div class="wordmark">Harbor720more</div>
    <ul class="service-list">
      <li>Finding sustainable employment for people over 50</li>
      <li>recruiting solutions for business</li>
      <li>training for individuals and orgnisations</li>
    </ul>
    <div class="website">www.harbor720more-demo.com.au</div>
    <div class="tagline-tab">Today is the day</div>
  </section>

  <section class="card card-back">
    <div class="mint-band"></div>
    <div class="partner-names">Dev, Mabel &amp; Joan</div>
    <div class="wordmark">Harbor720more</div>
    <address class="contact-list">
      Phone: 0498163520<br>
      Email: Harbor720more@mailbox-demo.com<br>
      Social/Harbor720more
    </address>
  </section>
</main>
</body>
</html>
```